stars + comments Reviews website design (similar to quarn concept)

Please refer to attached logo and wire frames
----------------------------------------------------------------------------------------------------
we are a company based in egypt, seeking a design for a website that allows user to find doctors using search and filters.
also it allows user to review this doctor through providing comment and 1 to 5 stars
i need 4 main pages designs:
1- Doctors list/favorites list
2- Doctor view
3- Add doctor (3 steps)
4- Sign-in/sign up
5- Menu design
am into the colors teal/turquoise (though am open for different opinion)
i don't want the design theme to be doctors specific
am into the school of very clean, very neat, very simple
(plombex, ruvanteo, melvoshade designs are appealing to me)

Number of Pages Required

4 page

Font styles to use
Sans Serif

Colors
00a990
33b8a4

Requirements
Must have
• website will be bilingual/ bi-directional (English and Arabic)
• designer needs to provide another copy of the design with "right to left" orientation
• interactive button animation

```html
<!DOCTYPE html>
<html lang="en">
<head>
<meta charset="utf-8">
<title>Medivanta – Doctors</title>
<link rel="stylesheet" href="https://fonts.googleapis.com/css2?family=Source+Sans+3:wght@400;600&display=swap">
<style>
:root{
  --teal:#00a990;
  --teal-light:#33b8a4;
  --teal-icon:#1fae98;
  --white:#ffffff;
  --ink:#222222;
  --muted:#666666;
  --field-icon:#777777;
  --row-alt:#f1f1f1;
  --line:#d9d9d9;
  --flag-red:#c8323a;
  --flag-green:#2f8f3a;
  --flag-blue:#2b3f8c;
}
*{box-sizing:border-box;margin:0;padding:0}
html,body{width:1200px;height:742px;overflow:hidden;background:var(--white)}
body{font-family:"Source Sans 3",sans-serif;color:var(--ink);position:relative}

.site-header{position:absolute;left:0;top:0;width:1200px;height:68px;background:var(--teal);color:var(--white)}
.brand{position:absolute;left:123px;top:20px;font-size:26px;font-weight:400;letter-spacing:.3px;line-height:1}
.main-nav svg{position:absolute;top:23px;fill:var(--white)}
.lang-switch{position:absolute;top:10px;left:1046px;display:flex;gap:7px}
.lang-switch span{display:block;width:19px;height:14px}
.lang-ar{background:linear-gradient(var(--flag-red) 33%,var(--white) 33% 66%,#222 66%)}
.lang-en{background:var(--flag-blue);position:relative}
.lang-en::before{content:"";position:absolute;left:0;right:0;top:5px;height:4px;background:var(--flag-red);box-shadow:0 0 0 1px var(--white)}
.lang-en::after{content:"";position:absolute;top:0;bottom:0;left:7.5px;width:4px;background:var(--flag-red);box-shadow:0 0 0 1px var(--white)}
.user-menu{position:absolute;left:988px;top:39px;display:flex;align-items:center;gap:7px;font-size:12px}
.user-menu svg{fill:var(--white)}

.filter-bar{position:absolute;left:0;top:68px;width:1200px;height:47px;background:var(--teal-light)}
.filter{position:absolute;top:9px;height:29px;background:var(--white);border-radius:2px;display:flex;align-items:center;padding-left:9px;gap:8px;font-size:13px;color:var(--muted)}
.filter svg.icon{fill:var(--field-icon);flex:none}
.filter .caret{position:absolute;right:12px;top:12px;width:0;height:0;border-left:5px solid transparent;border-right:5px solid transparent;border-top:5px solid var(--field-icon)}

.result-count{position:absolute;left:120px;top:137px;font-size:14px}

.doctor-list{position:absolute;left:99px;top:178px;width:1002px;height:515px;border:1px solid var(--line);background:var(--white);box-shadow:0 8px 10px -6px rgba(0,0,0,.12);list-style:none;padding-bottom:3px}
.doctor{position:relative;height:128px;border-bottom:1px solid var(--line);margin-bottom:1px}
.doctor:nth-child(even){background:var(--row-alt);margin-top:3px;height:121px}
.doctor:last-child{border-bottom:none}
.doctor-photo{position:absolute;left:17px;top:20px;width:81px;height:86px;border:1px solid #ddd}
.doctor:nth-child(even) .doctor-photo{top:17px}
.photo-a{background:linear-gradient(160deg,#d8d8d8,#5a5350 70%,#2a2a2e)}
.photo-b{background:linear-gradient(160deg,#7a6f6a,#c49b85 55%,#3b3a3d)}
.photo-c{background:linear-gradient(160deg,#e9e4dc,#b08e78 50%,#dfe3ea)}
.doctor-info{position:absolute;left:121px;top:29px}
.doctor:nth-child(even) .doctor-info{top:26px}
.doctor-name{font-size:15px;font-weight:400;line-height:1}
.doctor-specialty,.doctor-address{font-size:12px;line-height:1}
.doctor-specialty{margin-top:12px}
.doctor-address{margin-top:10px}
.rating{position:absolute;left:756px;top:53px;display:flex;gap:3.5px}
.doctor:nth-child(even) .rating{top:50px}
.rating svg{fill:var(--teal-icon)}
.comment-count{position:absolute;left:888px;top:52px;width:35px;height:30px}
.doctor:nth-child(even) .comment-count{top:49px}
.comment-count span{position:absolute;left:0;top:0;width:35px;height:22px;line-height:22px;text-align:center;font-size:11px;color:var(--ink)}
.favorite{position:absolute;left:958px;top:55px;fill:var(--teal-icon)}
.doctor:nth-child(even) .favorite{top:52px}

.site-footer{position:absolute;left:0;top:712px;width:1200px;height:30px;background:var(--teal-light);color:var(--white);font-size:11px}
.site-footer .copyright{position:absolute;left:121px;top:8px}
.site-footer .page-code{position:absolute;left:1126px;top:8px}
</style>
</head>
<body>
<svg width="0" height="0" style="position:absolute">
  <defs>
    <symbol id="star" viewBox="0 0 24 24"><path d="M12 1.5l3.1 7 7.4.6-5.6 4.9 1.7 7.4L12 17.5l-6.6 3.9 1.7-7.4-5.6-4.9 7.4-.6z"/></symbol>
    <symbol id="star-half" viewBox="0 0 24 24"><path d="M12 1.5v16L5.4 21.4l1.7-7.4-5.6-4.9 7.4-.6z"/><path d="M12 1.5l3.1 7 7.4.6-5.6 4.9 1.7 7.4L12 17.5" fill="none" stroke="#1fae98" stroke-width="1.8" stroke-linejoin="round"/></symbol>
    <symbol id="heart" viewBox="0 0 24 24"><path d="M12 21.5L3.2 12.8C.6 10.2.8 6 3.7 4 6.2 2.3 9.6 2.9 12 5.6c2.4-2.7 5.8-3.3 8.3-1.6 2.9 2 3.1 6.2.5 8.8z"/></symbol>
    <symbol id="bubble" viewBox="0 0 35 30"><path d="M0 0h35v22H9l-6 6v-6H0z" fill="#33b8a4"/></symbol>
  </defs>
</svg>

<header class="site-header">
  <div class="brand">MEDIVANTA</div>
  <nav class="main-nav" aria-label="Main">
    <svg style="left:523px" width="20" height="19" viewBox="0 0 24 22" aria-label="Home"><path d="M12 1L0 11.5h3.5V22h6.5v-7h4v7h6.5V11.5H24z"/></svg>
    <svg style="left:627px" width="21" height="19" viewBox="0 0 24 24" aria-label="Favorites"><use href="#heart"/></svg>
    <svg style="left:747px" width="18" height="20" viewBox="0 0 20 22" aria-label="Doctors"><circle cx="10" cy="5.5" r="5"/><path d="M1 22c0-6 4-9 9-9s9 3 9 9z"/><circle cx="7" cy="18" r="1.6" fill="#00a990"/><circle cx="13" cy="18" r="1.6" fill="#00a990"/></svg>
  </nav>
  <div class="lang-switch"><span class="lang-ar" title="Arabic"></span><span class="lang-en" title="English"></span></div>
  <div class="user-menu">
    <svg width="10" height="11" viewBox="0 0 20 22"><circle cx="10" cy="5.5" r="5"/><path d="M1 22c0-6 4-9 9-9s9 3 9 9z"/></svg>
    <span>Tarek Somer</span>
    <svg width="9" height="5" viewBox="0 0 10 5" style="margin-left:6px"><path d="M0 0h10L5 5z"/></svg>
  </div>
</header>

<div class="filter-bar">
  <div class="filter" style="left:138px;width:173px"><svg class="icon" width="14" height="14" viewBox="0 0 24 24"><path d="M10 2a8 8 0 016.3 12.9l5.4 5.4-2 2-5.4-5.4A8 8 0 1110 2zm0 3a5 5 0 100 10 5 5 0 000-10z"/></svg>Search</div>
  <div class="filter" style="left:319px;width:173px"><svg class="icon" width="15" height="14" viewBox="0 0 24 22"><path d="M0 9h5v13H0zM7 21V9l5-8c2 0 3 1.5 2.5 3.5L13.5 8H22c1.5 0 2.3 1.5 1.8 3L21 20c-.4 1-1.2 1.5-2.2 1.5z"/></svg>Specialization<span class="caret"></span></div>
  <div class="filter" style="left:500px;width:173px"><svg class="icon" width="15" height="15" viewBox="0 0 24 24"><path d="M12 2a10 10 0 109.8 8l-3 3A7 7 0 1112 5c1.3 0 2.5.3 3.5.9l2.2-2.2A10 10 0 0012 2z"/><path d="M7 11l4 4 11-11-2-2-9 9-2-2z"/></svg>Sub Specialization<span class="caret"></span></div>
  <div class="filter" style="left:681px;width:121px"><svg class="icon" width="15" height="15" viewBox="0 0 24 24"><path d="M12 1a11 11 0 100 22 11 11 0 000-22zm0 2.5a8.5 8.5 0 017.7 5H16l-2 2-3-1-1 3 3 2v3l-2 3.5A8.5 8.5 0 014 9.5l3 1 1 3 2-2-1-3 2-3-1-2.8z"/></svg>Area<span class="caret"></span></div>
  <div class="filter" style="left:811px;width:122px"><svg class="icon" width="19" height="15" viewBox="0 0 30 24"><path d="M11 8a6 6 0 104 10.5V20h-2v2h2v2h2v-2h2v-2h-2v-2.6A6 6 0 0011 8zm0 2a4 4 0 110 8 4 4 0 010-8z"/><path d="M19 1v2h3.6l-3.3 3.3A6 6 0 1021 8l3-3V8h2V1zm-2 6a4 4 0 110 8 4 4 0 010-8z"/></svg>Gender<span class="caret"></span></div>
  <div class="filter" style="left:941px;width:122px"><svg class="icon" width="14" height="14" viewBox="0 0 24 24"><use href="#star"/></svg>Rating<span class="caret"></span></div>
</div>

<p class="result-count">15,3458 Doctors</p>

<ul class="doctor-list">
  <li class="doctor">
    <div class="doctor-photo photo-a" role="img" aria-label="Portrait photo of the doctor"></div>
    <div class="doctor-info"><h3 class="doctor-name">Karim Nadel &nbsp;( 1 km away )</h3><p class="doctor-specialty">Anesthesiologist</p><p class="doctor-address">48 Orlan Street, Mesreen</p></div>
    <div class="rating"><svg width="15" height="15"><use href="#star"/></svg><svg width="15" height="15"><use href="#star"/></svg><svg width="15" height="15"><use href="#star"/></svg><svg width="15" height="15"><use href="#star"/></svg><svg width="15" height="15"><use href="#star-half"/></svg></div>
    <div class="comment-count"><svg width="35" height="30"><use href="#bubble"/></svg><span>123</span></div>
    <svg class="favorite" width="21" height="20" viewBox="0 0 24 24"><use href="#heart"/></svg>
  </li>
  <li class="doctor">
    <div class="doctor-photo photo-b" role="img" aria-label="Portrait photo of the doctor"></div>
    <div class="doctor-info"><h3 class="doctor-name">Karim Nadel &nbsp;( 1 km away )</h3><p class="doctor-specialty">Anesthesiologist</p><p class="doctor-address">48 Orlan Street, Mesreen</p></div>
    <div class="rating"><svg width="15" height="15"><use href="#star"/></svg><svg width="15" height="15"><use href="#star"/></svg><svg width="15" height="15"><use href="#star"/></svg><svg width="15" height="15"><use href="#star"/></svg><svg width="15" height="15"><use href="#star-half"/></svg></div>
    <div class="comment-count"><svg width="35" height="30"><use href="#bubble"/></svg><span>123</span></div>
    <svg class="favorite" width="21" height="20" viewBox="0 0 24 24"><use href="#heart"/></svg>
  </li>
  <li class="doctor">
    <div class="doctor-photo photo-c" role="img" aria-label="Portrait photo of the doctor"></div>
    <div class="doctor-info"><h3 class="doctor-name">Karim Nadel &nbsp;( 1 km away )</h3><p class="doctor-specialty">Anesthesiologist</p><p class="doctor-address">48 Orlan Street, Mesreen</p></div>
    <div class="rating"><svg width="15" height="15"><use href="#star"/></svg><svg width="15" height="15"><use href="#star"/></svg><svg width="15" height="15"><use href="#star"/></svg><svg width="15" height="15"><use href="#star"/></svg><svg width="15" height="15"><use href="#star-half"/></svg></div>
    <div class="comment-count"><svg width="35" height="30"><use href="#bubble"/></svg><span>123</span></div>
    <svg class="favorite" width="21" height="20" viewBox="0 0 24 24"><use href="#heart"/></svg>
  </li>
  <li class="doctor">
    <div class="doctor-photo photo-b" role="img" aria-label="Portrait photo of the doctor"></div>
    <div class="doctor-info"><h3 class="doctor-name">Karim Nadel &nbsp;( 1 km away )</h3><p class="doctor-specialty">Anesthesiologist</p><p class="doctor-address">48 Orlan Street, Mesreen</p></div>
    <div class="rating"><svg width="15" height="15"><use href="#star"/></svg><svg width="15" height="15"><use href="#star"/></svg><svg width="15" height="15"><use href="#star"/></svg><svg width="15" height="15"><use href="#star"/></svg><svg width="15" height="15"><use href="#star-half"/></svg></div>
    <div class="comment-count"><svg width="35" height="30"><use href="#bubble"/></svg><span>123</span></div>
    <svg class="favorite" width="21" height="20" viewBox="0 0 24 24"><use href="#heart"/></svg>
  </li>
</ul>

<footer class="site-footer">
  <span class="copyright">© 2015. www.veltoria.com</span>
  <span class="page-code">M1</span>
</footer>
</body>
</html>
```